Business Card for Modern Marketing Consultancy

Business card needed for marketing consultancy with existing logo.

Lanternway Co is a specialized boutique marketing consultancy that provides startup, small and mid size consumer businesses thought leadership and implementation of marketing strategies to help your business grow.

Our expertise, experience and industry knowledge stems from some of New York’s top global beauty and retail companies and allows us to draw from an array of successful marketing strategies and growth tactics tailored to suit the needs of your business

lanternwayco.example

Target Market(s)

start up, small and mid size consumer packaged goods businesses

Industry/Entity Type

Leadership

Requirements
Must have
• Must have the logo of the business and use of the exact colors of the logo.
Must be simple, sleek, modern and clean. Must make a statement and be eye catching.

Front: looking for unique design or visual statement with logo and tagline

Back of card should have:
logo - if not use on front.
Delia R. Horvath
Founder
Lanternway Co
m: 555.014.2276
deliahorvath@lanternwayco.example
lanternwayco.example

Please use the following words as these describe my services:
strategy analytics branding research

Please refer to the website look and feel: lanternwayco.example

Please kindly note that I am looking for a unique design that I cannot do myself with a template. thank you.
Nice to have
• Please also try and incorporate additional files attached.

```html
<!DOCTYPE html>
<html lang="en">
<head>
<meta charset="utf-8">
<title>Lanternway Co — Business Card</title>
<link href="https://fonts.googleapis.com/css2?family=Poiret+One&display=swap" rel="stylesheet">
<style>
  :root {
    --backdrop: #2a2a2a;
    --card-white: #f7f7f7;
    --magenta: #a8146e;
    --crimson: #cf1450;
    --logo-grey: #5e5e5e;
    --soft-pink: #ec9ccb;
  }
  * { margin: 0; padding: 0; box-sizing: border-box; }
  html, body {
    width: 1200px; height: 900px; overflow: hidden;
    background: var(--backdrop);
    font-family: "Poiret One", sans-serif;
  }
  .card {
    position: absolute;
    width: 560px; height: 320px;
    background: var(--card-white);
    overflow: hidden;
    box-shadow: 0 10px 30px rgba(0,0,0,.45);
  }
  .card svg { position: absolute; inset: 0; }
  .card-back { left: 320px; top: 100px; }
  .card-front { left: 320px; top: 480px; }

  .contact-name {
    position: absolute; left: 40px; top: 60px;
    font-size: 30px; color: var(--soft-pink); letter-spacing: .5px;
  }
  .contact-role {
    position: absolute; left: 40px; top: 100px;
    font-size: 19px; color: var(--soft-pink);
  }
  .contact-details {
    position: absolute; right: 34px; bottom: 34px;
    text-align: right; color: var(--magenta);
    font-size: 17px; line-height: 1.6;
  }

  .brand {
    position: absolute; left: 110px; top: 92px;
    display: flex; align-items: center; gap: 12px;
  }
  .brand-name {
    font-size: 40px; color: var(--logo-grey); letter-spacing: .5px;
  }
  .brand-dot {
    width: 22px; height: 22px; border-radius: 50%; background: var(--magenta);
  }
  .tagline {
    position: absolute; left: 120px; bottom: 52px;
    font-size: 27px; color: var(--soft-pink); letter-spacing: 1px;
  }
  .tagline-mark {
    position: absolute; left: 46px; bottom: 46px;
    width: 46px; height: 46px; border-radius: 50%; background: var(--card-white);
  }
</style>
</head>
<body>

  <section class="card card-back" aria-label="Card back">
    <svg viewBox="0 0 560 320" width="560" height="320" aria-hidden="true">
      <path d="M0,0 H560 V70 C420,90 260,205 0,220 Z" fill="var(--crimson)"/>
      <path d="M0,214 C260,199 420,84 560,64" fill="none" stroke="var(--card-white)" stroke-width="4"/>
      <path d="M0,0 H560 V50 C420,70 260,185 0,200 Z" fill="var(--magenta)"/>
    </svg>
    <div class="contact-name">Delia R. Horvath</div>
    <div class="contact-role">Founder</div>
    <div class="contact-details">
      <div>m: 555.014.2276</div>
      <div>deliahorvath@lanternwayco.example</div>
      <div>lanternwayco.example</div>
    </div>
  </section>

  <section class="card card-front" aria-label="Card front">
    <svg viewBox="0 0 560 320" width="560" height="320" aria-hidden="true">
      <path d="M0,196 C170,206 350,160 560,100 V320 H0 Z" fill="var(--crimson)"/>
      <path d="M0,214 C170,224 350,178 560,118" fill="none" stroke="var(--card-white)" stroke-width="4"/>
      <path d="M0,222 C170,232 350,186 560,126 V320 H0 Z" fill="var(--magenta)"/>
    </svg>
    <div class="brand">
      <span class="brand-name">Lanternway Co</span>
      <span class="brand-dot"></span>
    </div>
    <div class="tagline-mark"></div>
    <div class="tagline">Shape Your Brand With Purpose.</div>
  </section>

</body>
</html>
```